Gobal construction supply company needs new business card design

I need a business card design for my global supply company using an existing logo. i will be looking to print these on rounded corner cards with the black background version of my logo on the back. on the front white background, my logo again and my simple details.

```html
<!DOCTYPE html>
<html lang="en">
<head>
<meta charset="utf-8">
<title>Northgate Industrial – Business Card</title>
<link rel="stylesheet" href="https://fonts.googleapis.com/css2?family=Montserrat:wght@700&family=Open+Sans:wght@400&display=swap">
<style>
  :root {
    --canvas: #e6e6e6;
    --card-dark: #1c1c1c;
    --card-black: #050505;
    --card-white: #ffffff;
    --brand-red: #d40000;
    --text-dark: #333333;
    --text-light: #ffffff;
  }
  * { margin: 0; padding: 0; box-sizing: border-box; }
  html, body {
    width: 1200px;
    height: 782px;
    overflow: hidden;
    background: var(--canvas);
  }
  .stage {
    position: relative;
    width: 1200px;
    height: 782px;
    display: flex;
    flex-direction: column;
    align-items: center;
    justify-content: center;
    gap: 40px;
  }
  .card {
    position: relative;
    width: 600px;
    height: 343px;
    border-radius: 14px;
    overflow: hidden;
    box-shadow: 0 6px 18px rgba(0,0,0,0.25);
  }

  /* Back of card */
  .card-back {
    background: var(--card-dark);
    display: flex;
    align-items: center;
    justify-content: center;
  }
  .brand-name {
    font-family: 'Montserrat', sans-serif;
    font-weight: 700;
    font-size: 30px;
    letter-spacing: 0.5px;
    color: var(--text-light);
    text-transform: uppercase;
  }

  /* Front of card */
  .card-front { background: var(--card-white); }
  .front-shapes {
    position: absolute;
    inset: 0;
    width: 100%;
    height: 100%;
  }
  .shape-dark { fill: var(--card-dark); }
  .shape-black { fill: var(--card-black); }
  .shape-band { fill: var(--brand-red); }

  .person {
    position: absolute;
    right: 40px;
    top: 100px;
    text-align: right;
    color: var(--text-light);
  }
  .person-name {
    font-family: 'Montserrat', sans-serif;
    font-weight: 700;
    font-size: 24px;
    letter-spacing: 0.5px;
    text-transform: uppercase;
    line-height: 1.1;
  }
  .person-title {
    font-family: 'Open Sans', sans-serif;
    font-size: 15px;
    margin-top: 4px;
  }

  .contact-list {
    position: absolute;
    right: 22px;
    top: 222px;
    list-style: none;
    font-family: 'Open Sans', sans-serif;
    font-size: 16px;
    color: var(--text-dark);
  }
  .contact-item {
    display: flex;
    align-items: center;
    justify-content: flex-end;
    gap: 10px;
    height: 24px;
  }
  .contact-icon {
    width: 14px;
    height: 14px;
    fill: var(--brand-red);
    flex: none;
  }
</style>
</head>
<body>
<main class="stage">

  <section class="card card-back" aria-label="Card back">
    <span class="brand-name">Northgate Industrial</span>
  </section>

  <section class="card card-front" aria-label="Card front">
    <svg class="front-shapes" viewBox="0 0 600 343" preserveAspectRatio="none" aria-hidden="true">
      <polygon class="shape-dark" points="0,0 270,0 234,69 180,199 102,343 0,343"/>
      <polygon class="shape-black" points="234,69 270,0 327,69"/>
      <polygon class="shape-band" points="234,69 600,69 600,199 180,199"/>
    </svg>

    <div class="person">
      <div class="person-name">Daniel Hartley</div>
      <div class="person-title">Managing Director</div>
    </div>

    <ul class="contact-list">
      <li class="contact-item">
        <span>055-210 384 612</span>
        <svg class="contact-icon" viewBox="0 0 14 14" aria-hidden="true">
          <path d="M1 4 Q7 0 13 4 L11 6 L9 5 L9 4 Q7 3 5 4 L5 5 L3 6 Z"/>
          <rect x="3" y="7" width="8" height="6" rx="1"/>
        </svg>
      </li>
      <li class="contact-item">
        <span>055-210 384 640</span>
        <svg class="contact-icon" viewBox="0 0 14 14" aria-hidden="true">
          <path d="M3 1 H11 V13 H3 Z M4.5 2.5 V10.5 H9.5 V2.5 Z" fill-rule="evenodd"/>
        </svg>
      </li>
      <li class="contact-item">
        <span>info@ngindustrial.example</span>
        <svg class="contact-icon" viewBox="0 0 14 14" aria-hidden="true">
          <path d="M1 3 H13 V11 H1 Z M2 4 L7 8 L12 4 Z" fill-rule="evenodd"/>
        </svg>
      </li>
      <li class="contact-item">
        <span>www.ngindustrial.example</span>
        <svg class="contact-icon" viewBox="0 0 14 14" aria-hidden="true">
          <circle cx="7" cy="7" r="6"/>
        </svg>
      </li>
    </ul>
  </section>

</main>
</body>
</html>
```